LumaMove In-home Personal Training

I would like to have some eye-catching business card design. Opened to any ideas.

The business idea: mobile fitness - train clients at their places

Target Market(s)

General population, 20-60 years old

Industry/Entity Type

Fitness

Contact Information for Business Card

The information to include:
Name: Marta
Call or text: 306-555-0187
Website: LumaMove.ca
Please use the attached logo

Requirements
Should not have
• No orange or purple colours please

```html
<!DOCTYPE html>
<html lang="en">
<head>
<meta charset="utf-8">
<title>LumaMove Business Card</title>
<link rel="stylesheet" href="https://fonts.googleapis.com/css2?family=Arimo:wght@400;700&family=Lato:wght@300;400&display=swap">
<style>
  :root {
    --backdrop: #d6d6d6;
    --card: #1f1f21;
    --contact-grey: #6b6b6d;
    --deco-grey: #2c2c2e;
    --brand-grey: #8e8e90;
    --subtitle-grey: #4a4a4c;
    --tagline-grey: #b4b4b6;
  }
  * { box-sizing: border-box; margin: 0; padding: 0; }
  html, body { width: 1200px; height: 802px; overflow: hidden; }
  body { background: var(--backdrop); position: relative; }
  .card {
    position: absolute;
    top: 274px;
    width: 442px;
    height: 264px;
    background: var(--card);
    border-radius: 12px;
    overflow: hidden;
  }
  .card--front { left: 136px; }
  .card--back { left: 625px; }

  .front-deco {
    position: absolute;
    left: -40px;
    top: 30px;
    width: 260px;
    height: 260px;
    border: 6px solid var(--deco-grey);
    border-radius: 50%;
  }
  .contact {
    position: absolute;
    left: 260px;
    top: 128px;
    font-family: "Arimo", Arial, sans-serif;
    color: var(--contact-grey);
    white-space: nowrap;
  }
  .contact__name {
    font-size: 21px;
    font-weight: 700;
    letter-spacing: 0.5px;
    margin-bottom: 20px;
  }
  .contact__row {
    display: flex;
    align-items: center;
    gap: 5px;
    font-size: 16px;
    height: 22px;
    margin-bottom: 11px;
  }
  .contact__icon { width: 19px; height: 19px; flex: none; }

  .brand {
    position: absolute;
    left: 0; right: 0;
    top: 98px;
    display: flex;
    justify-content: center;
    align-items: center;
    gap: 12px;
  }
  .brand__mark {
    width: 18px; height: 18px;
    border: 2px solid var(--brand-grey);
  }
  .brand__text {
    display: flex;
    flex-direction: column;
    align-items: stretch;
  }
  .brand__name {
    font-family: "Lato", sans-serif;
    font-weight: 300;
    font-size: 38px;
    line-height: 40px;
    letter-spacing: 3px;
    color: var(--brand-grey);
  }
  .brand__subtitle {
    font-family: "Lato", sans-serif;
    font-weight: 400;
    font-size: 7.5px;
    letter-spacing: 2.6px;
    text-transform: uppercase;
    text-align: right;
    color: var(--subtitle-grey);
    margin-top: 2px;
    white-space: nowrap;
  }
  .tagline {
    position: absolute;
    left: 0; right: 0;
    top: 213px;
    text-align: center;
    font-family: "Lato", sans-serif;
    font-size: 15px;
    color: var(--tagline-grey);
  }
  .tagline__dot {
    display: inline-block;
    width: 6px; height: 6px;
    border-radius: 50%;
    background: var(--tagline-grey);
    margin: 0 5px;
    vertical-align: middle;
  }
</style>
</head>
<body>
  <section class="card card--front">
    <div class="front-deco" aria-hidden="true"></div>
    <div class="contact">
      <p class="contact__name">MARTA</p>
      <p class="contact__row">
        <svg class="contact__icon" viewBox="0 0 20 20" aria-hidden="true">
          <rect x="1.5" y="1.5" width="17" height="17" rx="2" fill="none" stroke="#6b6b6d" stroke-width="1.6"/>
          <path d="M6.5 4.5 L8.5 4.5 L9.2 7.5 L7.8 8.5 Q9 11.5 11.5 12.5 L12.5 11 L15.5 11.8 L15.5 13.8 Q15 15.5 13 15.5 Q5 14.5 4.5 6.5 Q4.6 4.6 6.5 4.5 Z" fill="#6b6b6d"/>
        </svg>
        306-555-0187
      </p>
      <p class="contact__row">
        <svg class="contact__icon" viewBox="0 0 20 20" aria-hidden="true">
          <g fill="none" stroke="#6b6b6d" stroke-width="1.5">
            <circle cx="10" cy="10" r="8.5"/>
            <ellipse cx="10" cy="10" rx="3.8" ry="8.5"/>
            <line x1="1.5" y1="10" x2="18.5" y2="10"/>
            <path d="M3 5.5 H17 M3 14.5 H17"/>
          </g>
        </svg>
        www.LumaMove.ca
      </p>
    </div>
  </section>

  <section class="card card--back">
    <div class="brand">
      <span class="brand__mark" aria-hidden="true"></span>
      <div class="brand__text">
        <span class="brand__name">LumaMove</span>
        <span class="brand__subtitle">In-home personal training</span>
      </div>
    </div>
    <p class="tagline">Mobile Fitness<span class="tagline__dot"></span>Train clients at their places</p>
  </section>
</body>
</html>
```